I need a general brochure for a new non-profit committed to empowering survivors of sexual exploitation. I kept the wording to a minimum so the design will help me tell the story. The brochure will be used in churches and other venues when I give presentations. I will also be using this in one on one presentations to walk through the highlights of our work. We are in the aftercare business and the feel should communicate hope and new beginnings.

I would like a single fold brochure- about 8.5x5.5.
Updates

to clarify- the brochure should be 8.5 by 5.5 Added Wednesday, November 05, 2014

Target Market(s)

donors, volunteers- all ages- mainly women

Industry/Entity Type

Non-Profit

Font styles to use
Serif

Requirements
Must have
• Pictures draw me in. I tend to like professional designs with just enough color and detail to make them unique.
• Hopeful- note the picture I attached are bright- not sad and depressed. Feel free to add your own photos if they are better. My favorite picture is the black woman with sun.
• Please use a variety of races- we serve a diverse population.
• I also need my website listed www.brightmorrowhaven.org
Nice to have
• I have seen some designs that use one picture to stretch across the front and back of the brochure. This might be interesting if it works, but I may have too much text on the back to make this worthwhile.
Should not have
• hearts, country feel, goofy, whimsical

```html
<!DOCTYPE html>
<html lang="en">
<head>
<meta charset="utf-8">
<title>Bright Morrow Haven – Brochure Inside Spread</title>
<link rel="stylesheet" href="https://fonts.googleapis.com/css2?family=Della+Respira&family=Lora:wght@400;700&family=Merriweather:wght@700;900&display=swap">
<style>
  :root {
    --cream: #fbe6bf;
    --cream-light: #fbf1cf;
    --sage: #e6eab8;
    --navy: #1f3f66;
    --teal: #1c5868;
    --maroon: #3e1424;
    --ink: #3a1420;
    --mission-bg: #f8d9a4;
  }
  * { margin: 0; padding: 0; box-sizing: border-box; }
  html, body { width: 1200px; height: 776px; overflow: hidden; }
  body {
    position: relative;
    background: linear-gradient(120deg, var(--cream) 0%, var(--cream-light) 55%, var(--sage) 100%);
    font-family: "Lora", Georgia, serif;
    color: var(--ink);
  }
  .photo-band { position: absolute; inset: 0; width: 1200px; height: 776px; }
  .mission-box {
    position: absolute; left: 264px; top: 262px; width: 285px; height: 166px;
    background: var(--mission-bg); border-radius: 18px;
    padding: 12px 14px 0 20px; color: var(--navy);
    font-family: "Merriweather", Georgia, serif; font-weight: 700;
    font-size: 16.5px; line-height: 1.32;
  }
  .mission-box .label {
    font-size: 42px; font-weight: 900; line-height: 1; margin-left: 4px;
  }
  .website {
    position: absolute; left: 341px; top: 438px;
    font-size: 19px; color: var(--ink); letter-spacing: 0.3px;
  }
  .model { position: absolute; left: 62px; top: 402px; width: 520px; }
  .model h2 {
    font-family: "Merriweather", Georgia, serif; font-weight: 700;
    font-size: 29px; color: var(--maroon); margin-left: 4px; margin-bottom: 10px;
  }
  .model h3 {
    font-family: "Merriweather", Georgia, serif; font-weight: 700;
    font-size: 19px; color: var(--maroon); margin-bottom: 2px;
  }
  .model p { font-size: 16.5px; line-height: 1.3; color: var(--ink); margin-bottom: 5px; }
  .vision { position: absolute; right: 62px; top: 30px; text-align: right; color: var(--teal); }
  .vision h2 {
    font-family: "Merriweather", Georgia, serif; font-weight: 900;
    font-size: 52px; line-height: 1; margin-bottom: 6px;
  }
  .vision p {
    font-family: "Merriweather", Georgia, serif; font-weight: 700;
    font-size: 19px; line-height: 1.3; width: 250px; text-align: left;
  }
  .vision p span { display: block; }
  .roles {
    position: absolute; left: 640px; top: 250px; width: 475px; text-align: center;
    font-family: "Della Respira", Georgia, serif; color: var(--ink);
  }
  .roles .title { font-size: 38px; margin-left: 170px; line-height: 1; }
  .roles h3 { font-size: 25px; font-weight: 400; line-height: 1.1; }
  .roles .first { text-align: left; margin: -10px 0 0 165px; }
  .roles p { font-size: 16.5px; line-height: 1.45; margin-bottom: 16px; }
</style>
</head>
<body>
  <svg class="photo-band" viewBox="0 0 1200 776" aria-hidden="false">
    <defs>
      <linearGradient id="photoTone" x1="0" y1="0" x2="1" y2="0.4">
        <stop offset="0" stop-color="#6e4a34"/>
        <stop offset="0.35" stop-color="#caa088"/>
        <stop offset="0.65" stop-color="#8f6a54"/>
        <stop offset="1" stop-color="#d9b89a"/>
      </linearGradient>
      <linearGradient id="sweep" x1="0" y1="0" x2="1" y2="1">
        <stop offset="0" stop-color="#fbe6bf" stop-opacity="0.7"/>
        <stop offset="1" stop-color="#fbe6bf" stop-opacity="0"/>
      </linearGradient>
    </defs>
    <path role="img" aria-label="Photo of three smiling young women laughing together"
          d="M0,0 H950 C880,140 780,270 620,318 C450,360 250,300 0,340 Z" fill="url(#photoTone)"/>
    <path d="M0,340 C250,300 450,360 620,318 C780,270 880,140 950,0 H985 C900,170 800,300 640,345 C430,400 230,330 0,380 Z"
          fill="url(#sweep)"/>
  </svg>

  <div class="mission-box">
    Mobilize communities to encourage and equip survivors of sexual exploitation to build new lives. <span class="label">Mission</span>
  </div>

  <div class="website">www.brightmorrowhaven.org</div>

  <section class="model">
    <h2>Our Model</h2>
    <h3>Heal</h3>
    <p>Survivors need safe relationships and a safe environment to heal. Bright Morrow Haven facilitates mentor relationships, offers a supportive community and immerses survivors in faith-based curriculum.</p>
    <h3>Discover</h3>
    <p>In order to thrive, survivors need to discover their innate ability, preferences, personality and spiritual gifts.</p>
    <h3>Overcome</h3>
    <p>Survivors overcome barriers to moving ahead with the right educational and employment options.</p>
  </section>

  <section class="vision">
    <h2>Vision</h2>
    <p>
      <span style="padding-left:30px">Survivors of</span>
      <span style="padding-left:48px">sexual exploitation</span>
      <span style="padding-left:40px">live free, fulfilling</span>
      <span style="padding-left:22px">their God-given</span>
      <span>purpose.</span>
    </p>
  </section>

  <section class="roles">
    <div class="title">Your Role</div>
    <h3 class="first">Mentor</h3>
    <p>Build a safe nurturing relationship with one woman and encourage her to reach her goals. Join a community who receive training and support to effectively mentor.</p>
    <h3>Teacher</h3>
    <p>Teach group classes on life skills, biblical studies, physical wellbeing, creative arts, conflict resolution, emotional health, literacy, and financial management.</p>
    <h3>Business Partner</h3>
    <p style="margin-bottom:4px">Provide employment and business coaching to a survivor.</p>
    <h3>Supporter</h3>
    <p>Financially and prayerfully support the work of Bright Morrow Haven.</p>
  </section>
</body>
</html>
```